Spring OBRu 2016 Training Weekend Program Booklet

We need graphic design for the program booklet for our Spring leadership development training weekend for minority MBA students working in Finance. The design should include the colors in the attached logo and be fun and young (but somewhat conservative). The final files should be either Adobe InDesign or Illustrator so we can lay in text and images as needed. The layout will be:
Front Cover
Interior Page Template with Design
Inside Front Cover - Table of Contents
Page 1. Welcome Letter
Pages 2-3. Sponsor Acknowledgement
Pages 4-5. Program Agenda
Page 6. Listing of speakers and presenters
Page 7. Upcoming Events (Calendar)
Pages 8-10 Student Directory
Page 11. Listing of School Captains
Page 12. Resource Documents (title page)
Pages 13-16 Resource Documents
Pages 17 - 24. Notes Pages (blank for taking notes)
A sample of last season's book is provided.
Target Market(s)
Minority business school students attending top business schools (i.e Bellmore, Tresdin, Pelgrave, etc.)
Industry/Entity Type
Financial Service

```html
<!DOCTYPE html>
<html lang="en">
<head>
<meta charset="utf-8">
<title>Fall OBRu Weekend – Program Booklet Spreads</title>
<link rel="stylesheet" href="https://fonts.googleapis.com/css2?family=Arimo:wght@400&family=Roboto:wght@300&display=swap">
<style>
:root{
  --mint:#5fe3a8;
  --lime:#b5e61d;
  --teal:#4fc6c6;
  --pale:#d4f5e8;
  --ink:#1e1e1e;
  --rule:#cfcfcf;
  --logo-box:#e6e8e8;
}
*{margin:0;padding:0;box-sizing:border-box}
html,body{width:1200px;height:1200px;overflow:hidden;background:#fff}
.canvas{position:relative;width:1200px;height:1200px;background:#fff}
.page{position:absolute;width:348px;height:630px;background:#fff;border:1px solid var(--rule);overflow:hidden}
.page--toc{left:66px;top:10px}
.page--welcome{left:440px;top:10px;border-color:#222}
.page--sponsor-a{left:835px;top:10px}
.page--sponsor-b{left:86px;top:664px;transform:scale(.818);transform-origin:0 0}
.page-header{position:absolute;left:0;top:0;width:348px;height:62px;background:linear-gradient(180deg,var(--lime) 0%,var(--mint) 48%,var(--teal) 100%)}
.photo{position:absolute;left:0;top:0;width:348px;height:630px}
.photo--group{clip-path:polygon(166px 0,348px 0,348px 190px,254px 190px);background:linear-gradient(135deg,#d6ee8a,#9fcb4f 60%,#7ea83d)}
.photo--speaker{clip-path:polygon(254px 190px,348px 190px,348px 392px);background:linear-gradient(160deg,#c9b89c,#7d6f60 55%,#3b3734)}
.photo--pair{clip-path:polygon(157px 0,348px 0,348px 126px,219px 126px);background:linear-gradient(135deg,#bcae98,#8d7d69 60%,#b7b0a6)}
.photo--crowd{clip-path:polygon(219px 126px,348px 126px,348px 386px);background:linear-gradient(160deg,#4fa08d,#2b5f53 55%,#1b2723)}
.page-title{position:absolute;font-family:"Roboto",sans-serif;font-weight:300;color:var(--teal);font-size:21px;line-height:20px}
.toc-title{left:24px;top:218px}
.welcome-title{left:0;width:100%;text-align:center;top:180px}
.sponsor-title{left:43px;top:204px}
.toc-list{position:absolute;left:25px;top:266px;list-style:none}
.toc-list li{display:flex;align-items:center;height:19.7px;font-family:"Arimo",sans-serif;font-size:8px;color:var(--ink)}
.toc-list li::before{content:"";width:11px;height:11px;border-radius:50%;background:var(--teal);margin-right:9px}
.toc-list li:nth-child(even)::before{background:var(--lime)}
.body-copy{position:absolute;font-family:"Arimo",sans-serif;font-size:6.6px;line-height:11px;color:var(--ink)}
.body-copy p+p{margin-top:11px}
.welcome-copy{left:42px;top:241px;width:266px}
.sponsor-copy{left:29px;top:272px;width:132px;font-size:7px}
.signature{position:absolute;left:216px;top:429px;width:88px;height:66px;background:linear-gradient(180deg,#f4f4f4,#e9e9e9)}
.signer{position:absolute;left:236px;top:505px;font-family:"Arimo",sans-serif;font-size:6.6px;color:var(--ink)}
.logo-grid{position:absolute;left:29px;top:468px;display:grid;grid-template-columns:repeat(3,70px);column-gap:12px;row-gap:12px}
.logo-slot{height:22px;background:var(--logo-box);font-family:"Arimo",sans-serif;font-size:8px;color:#444;display:flex;align-items:center;justify-content:center}
.event-name{position:absolute;left:0;width:100%;top:588px;text-align:center;font-family:"Arimo",sans-serif;font-size:9px;line-height:10px;color:var(--teal)}
.event-date{position:absolute;left:0;width:100%;top:601px;text-align:center;font-family:"Arimo",sans-serif;font-size:4px;color:var(--ink)}
.page-number{position:absolute;right:18px;top:574px;font-family:"Roboto",sans-serif;font-weight:300;font-size:36px;color:#eef3f2}
.footer-band{position:absolute;left:0;bottom:0;width:100%;height:13px;background:var(--mint)}
</style>
</head>
<body>
<main class="canvas">

  <section class="page page--toc">
    <div class="page-header" role="img" aria-label="Decorative header pattern in lime, mint and teal"></div>
    <div class="photo photo--group" role="img" aria-label="Photo of smiling students at the training weekend"></div>
    <div class="photo photo--speaker" role="img" aria-label="Photo of a guest speaker in a suit"></div>
    <h2 class="page-title toc-title">Table of Contents</h2>
    <ul class="toc-list">
      <li>Lorem Ipsum is simply dummy text</li>
      <li>Lorem Ipsum is simply dummy text</li>
      <li>Lorem Ipsum is simply dummy text</li>
      <li>Lorem Ipsum is simply dummy text</li>
      <li>Lorem Ipsum is simply dummy text</li>
      <li>Lorem Ipsum is simply dummy text</li>
      <li>Lorem Ipsum is simply dummy text</li>
      <li>Lorem Ipsum is simply dummy text</li>
      <li>Lorem Ipsum is simply dummy text</li>
      <li>Lorem Ipsum is simply dummy text</li>
      <li>Lorem Ipsum is simply dummy text</li>
      <li>Lorem Ipsum is simply dummy text</li>
    </ul>
    <div class="event-name">Fall OBRu Weekend</div>
    <div class="event-date">September 11-13, 2016</div>
    <div class="footer-band"></div>
  </section>

  <section class="page page--welcome">
    <div class="page-header" role="img" aria-label="Decorative header pattern in lime, mint and teal"></div>
    <h2 class="page-title welcome-title">Welcome Letter</h2>
    <div class="body-copy welcome-copy">
      <p>ontrary to popular belief, Lorem Ipsum is not simply random text. It has roots in a piece of classical Latin literature from 45 BC, making it over 2000 years old. Rowan Delacourt, a Latin professor at Marlow Hill College in Virginia, looked up one of the more obscure Latin words, consectetur, from a Lorem Ipsum passage, and going through the cites of the word in classical literature, discovered the undoubtable source. Lorem Ipsum comes from sections 1.10.32 and 1.10.33 of "de Finibus Bonorum et Malorum" (The Extremes of Good and Evil) by Corvane, written in 45 BC. This book is a treatise on the theory of ethics, very popular during the Renaissance. The first line of Lorem Ipsum, "Lorem ipsum dolor sit amet..", comes from a line in section 1.10.32.</p>
      <p>The standard chunk of Lorem Ipsum used since the 1500s is reproduced below for those interested. Sections 1.10.32 and 1.10.33 from "de Finibus Bonorum et Malorum" by Corvane are also reproduced in their exact original form, accompanied by English versions from the 1914 translation by H. Rennick.</p>
    </div>
    <div class="signature" role="img" aria-label="Handwritten signature of the letter's author"></div>
    <div class="signer">Mr. Terrence Vale</div>
    <div class="event-name">Fall OBRu Weekend</div>
    <div class="event-date">September 11-13, 2016</div>
    <div class="page-number">1</div>
    <div class="footer-band"></div>
  </section>

  <section class="page page--sponsor-a">
    <div class="page-header" role="img" aria-label="Decorative header pattern in lime, mint and teal"></div>
    <div class="photo photo--pair" role="img" aria-label="Photo of two smiling program participants"></div>
    <div class="photo photo--crowd" role="img" aria-label="Photo of students gathered at an evening event"></div>
    <h2 class="page-title sponsor-title">Sponsor<br>Acknowledgement</h2>
    <div class="body-copy sponsor-copy">
      <p>ontrary to popular belief, Lorem Ipsum is not simply random text. It has roots in a piece of classical Latin literature from 45 BC, making it over 2000 years old. Rowan Delacourt, a Latin professor at Marlow Hill College in Virginia, looked up one of the more obscure Latin words, consectetur, from a Lorem Ipsum passage, and going through the cites of the word in classical literature, discovered the undoubtable source. Lorem Ipsum comes from sections 1.10.32 and 1.10.33 of "de Finibus Bonorum et Malorum" (The Extremes of Good and Evil) by Corvane, written in 45 BC. This book is a treatise on the theory of ethics, very popular during the</p>
    </div>
    <div class="logo-grid">
      <div class="logo-slot">logos</div><div class="logo-slot">logos</div><div class="logo-slot">logos</div>
      <div class="logo-slot">logos</div><div class="logo-slot">logos</div><div class="logo-slot">logos</div>
    </div>
    <div class="event-name">Fall OBRu Weekend</div>
    <div class="event-date">September 11-13, 2016</div>
    <div class="page-number">2</div>
    <div class="footer-band"></div>
  </section>

  <section class="page page--sponsor-b">
    <div class="page-header" role="img" aria-label="Decorative header pattern in lime, mint and teal"></div>
    <div class="photo photo--pair" role="img" aria-label="Photo of two smiling program participants"></div>
    <div class="photo photo--crowd" role="img" aria-label="Photo of students gathered at an evening event"></div>
    <h2 class="page-title sponsor-title">Sponsor<br>Acknowledgement</h2>
    <div class="body-copy sponsor-copy">
      <p>ontrary to popular belief, Lorem Ipsum is not simply random text. It has roots in a piece of classical Latin literature from 45 BC, making it over 2000 years old. Rowan Delacourt, a Latin professor at Marlow Hill College in Virginia, looked up one of the more obscure Latin words, consectetur, from a Lorem Ipsum passage, and going through the cites of the word in classical literature, discovered the undoubtable source. Lorem Ipsum comes from sections 1.10.32 and 1.10.33 of "de Finibus Bonorum et Malorum" (The Extremes of Good and Evil) by Corvane, written in 45 BC. This book is a treatise on the theory of ethics, very popular during the</p>
    </div>
    <div class="logo-grid">
      <div class="logo-slot">logos</div><div class="logo-slot">logos</div><div class="logo-slot">logos</div>
      <div class="logo-slot">logos</div><div class="logo-slot">logos</div><div class="logo-slot">logos</div>
    </div>
    <div class="event-name">Fall OBRu Weekend</div>
    <div class="event-date">September 11-13, 2016</div>
    <div class="page-number">3</div>
    <div class="footer-band"></div>
  </section>

</main>
</body>
</html>
```